Task and Project Management Tool Website

We need designs for both desktop and mobile for a new site, which is the marketing presentation of our new platform called Tilebeam, which is a task and project tool specific for the property sector. The name refers to people working on different workstreams on a property and crossing their paths when collaborating. The site will not do ecommerce, just a presentation of the product. We would like to include a video (no voice over) and some graphics, which we will do separately. The whole site will include a few pages, as detailed in the attach document. The product appeals to property companies and banks, hence the brand should portray reliability, corporate. We would like to see combinations of black, white and blue.
Updates

This project is currently put on hold. Client will be focusing on getting a Logo design first. Then once the logo has been created, we will resume this project and use the logo on the web designs submissions. Regards, DC Admin Osgood

Logo design has been completed. Please resubmit and submit new web designs on this project using the logo design attached. Regards, DC Admin Osgood

Target Market(s)

Corporate (B2B)

Logo Text

Tilebeam

Coding

Coded - Design and coding required

Number of Pages Required

5+ page

Requirements
Must have
• As in the specs
Should not have
• pictures of fake people (we prefer icons)

```html
<!DOCTYPE html>
<html lang="en">
<head>
<meta charset="utf-8">
<title>Tilebeam — Task and Project Management</title>
<link href="https://fonts.googleapis.com/css2?family=Roboto:wght@300;400;500;700&family=Lato:wght@400&family=Poppins:wght@400;500&display=swap" rel="stylesheet">
<style>
:root{
  --blue:#0b3d91;
  --blue-deep:#062a6e;
  --blue-mid:#1552b3;
  --blue-link:#1a5fc8;
  --ink:#222a33;
  --text:#3b4350;
  --muted:#6d7480;
  --light:#eef3f8;
  --white:#ffffff;
  --footer:#050505;
  --footer-bar:#1f1f1f;
  --star:#f08a1c;
}
*{box-sizing:border-box;margin:0;padding:0}
html,body{width:1200px;height:3511px;overflow:hidden}
body{position:relative;background:var(--white);font-family:'Roboto',sans-serif;color:var(--text)}
.abs{position:absolute}
a{color:inherit;text-decoration:none}

/* Header */
.site-header{left:0;top:0;width:1200px;height:85px;background:var(--white)}
.brand{display:flex;align-items:center;gap:12px;font-weight:500;font-size:33px;color:var(--blue)}
.brand-square{width:52px;height:52px;background:var(--blue)}
.site-header .brand{left:116px;top:16px}
.main-nav a{position:absolute;top:30px;font-size:19px;color:var(--ink)}
.main-nav a.active{color:var(--blue-link)}
.main-nav a.active::after{content:"";position:absolute;left:50%;margin-left:-12px;bottom:-9px;width:24px;height:2px;background:var(--blue-link)}

/* Hero */
.hero{left:0;top:85px;width:1200px;height:610px;background:linear-gradient(100deg,#0a4bb0 0%,#0b3f98 45%,#0a2f78 100%)}
.hero-title{left:121px;top:160px;font-size:44px;font-weight:500;line-height:47px;color:var(--white)}
.hero-text{left:121px;top:270px;width:400px;font-size:15.5px;line-height:27px;color:#e6eeff}
.btn{display:flex;align-items:center;justify-content:center;font-family:'Roboto',sans-serif;font-weight:500;border:2px solid;border-radius:3px;text-transform:uppercase}
.btn-light{color:var(--white);border-color:var(--white)}
.btn-blue{color:var(--blue);border-color:var(--blue)}
.hero .btn{left:124px;top:370px;width:159px;height:48px;font-size:16px}
.hero-dashboard{left:567px;top:121px;width:486px;height:362px;background:#f4f6fb;box-shadow:0 8px 30px rgba(0,0,0,.3)}
.hero-arrow{top:255px}

/* Intro */
.intro-title{left:0;top:756px;width:1200px;text-align:center;font-size:43px;font-weight:400;color:var(--ink)}
.intro-text{left:200px;top:822px;width:800px;text-align:center;font-size:17.5px;line-height:27px;color:var(--text)}
.feature-card{top:926px;width:283px;height:293px;border:2px solid #e1e5ea;background:var(--white);text-align:center}
.feature-card.is-featured{background:var(--blue);border-color:var(--blue)}
.feature-card svg{position:absolute;left:50%;top:34px;transform:translateX(-50%)}
.feature-card h3{position:absolute;left:0;right:0;top:125px;font-size:24px;font-weight:400;color:var(--blue)}
.feature-card p{position:absolute;left:20px;right:20px;top:163px;font-size:14.5px;line-height:20px;color:var(--text)}
.feature-card.is-featured h3{color:var(--white)}
.feature-card.is-featured p{color:#dbe6ff}
.feature-card .btn{position:absolute;left:70px;top:223px;width:143px;height:44px;font-size:14px}

/* Video */
.band-light{left:0;top:1556px;width:1200px;height:616px;background:var(--light)}
.video-frame{left:317px;top:1283px;width:596px;height:350px;background:linear-gradient(135deg,#39414a,#1d2226 60%,#3a3326);box-shadow:0 6px 20px rgba(0,0,0,.25)}
.play-button{left:574px;top:1411px}

/* Why */
.why-photo{left:0;top:1640px;width:640px;height:532px;background:linear-gradient(90deg,#8fa0b6 0%,#a8b6c9 55%,var(--light) 100%)}
.why-title{left:636px;top:1738px;font-size:36px;font-weight:500;color:var(--ink)}
.why-text{left:640px;width:460px;font-size:16px;line-height:27px;color:var(--text)}
.why .btn{left:643px;top:2024px;width:170px;height:51px;font-size:17px}

/* Testimonials */
.testi-title{left:0;top:2222px;width:1200px;text-align:center;font-size:36px;font-weight:500;color:var(--ink)}
.testi-card{left:297px;top:2294px;width:572px;height:301px;background:var(--white);border:2px solid #e3e6ea;box-shadow:0 2px 8px rgba(0,0,0,.08)}
.avatar{left:252px;top:30px;width:68px;height:68px;border-radius:50%;background:linear-gradient(#d8dbe0,#b7bcc4)}
.quote-mark{font-family:Georgia,serif;font-size:48px;font-weight:700;color:var(--blue);font-style:italic}
.testi-quote{left:55px;top:106px;width:462px;text-align:center;font-family:'Lato',sans-serif;font-size:14px;line-height:23px;color:var(--muted)}
.stars{left:0;width:100%;top:186px;display:flex;justify-content:center;gap:8px}
.testi-name{left:0;width:100%;top:227px;text-align:center;font-family:'Poppins',sans-serif;font-size:15px;font-weight:500;color:var(--ink)}
.testi-role{left:0;width:100%;top:246px;text-align:center;font-family:'Poppins',sans-serif;font-size:15px;color:var(--muted)}

/* Access */
.access{left:0;top:2667px;width:1200px;height:473px;background:linear-gradient(100deg,#1257b8 0%,#1150ad 45%,#0f3e8a 75%,#0b2c63 100%)}
.access-title{left:147px;top:105px;font-size:35px;font-weight:400;color:var(--white)}
.access-text{left:149px;width:470px;font-size:14.5px;line-height:23px;color:#e6eeff}
.access .btn{left:148px;top:331px;width:156px;height:47px;font-size:15px}

/* Footer */
.site-footer{left:0;top:3140px;width:1200px;height:313px;background:var(--footer);color:var(--white)}
.site-footer .brand{left:147px;top:65px;color:var(--white);font-weight:400;font-size:35px}
.site-footer .brand-square{background:var(--white);width:54px;height:54px}
.footer-about{left:147px;top:143px;width:280px;font-size:12px;line-height:23px;color:#d0d0d0}
.footer-col h4{font-size:20px;font-weight:400;margin-bottom:4px}
.footer-col li{list-style:none;font-size:15px;line-height:27px;color:#d8d8d8}
.social{display:flex;gap:6px;margin-top:10px}
.social span{width:37px;height:37px;border:2px solid var(--white);border-radius:50%}
.footer-bar{left:0;top:3453px;width:1200px;height:58px;background:var(--footer-bar);text-align:center;line-height:58px;font-size:13px;color:#9a9a9a}
</style>
</head>
<body>

<header class="site-header abs">
  <a class="brand abs" href="#"><span class="brand-square"></span>Tilebeam</a>
  <nav class="main-nav">
    <a class="active" href="#" style="left:511px">Product</a>
    <a href="#" style="left:631px">Services</a>
    <a href="#" style="left:756px">About</a>
    <a href="#" style="left:851px">Resources</a>
    <a href="#" style="left:983px">Contact Us</a>
  </nav>
</header>

<section class="hero abs">
  <h1 class="hero-title abs">Easiest way to<br>Collaborate</h1>
  <p class="hero-text abs">Curabitur vel mi sit amet magna malesuada ultrices Ut nisi erat fermentum vel congue id euismod in elit Fusce ultricies orci ac feugiat suscip</p>
  <a class="btn btn-light abs" href="#">Learn More</a>
  <div class="hero-dashboard abs" role="img" aria-label="Screenshot of the Tilebeam dashboard with charts and summary panels"></div>
  <svg class="hero-arrow abs" style="left:26px" width="26" height="44" viewBox="0 0 26 44"><path d="M20 6 6 22l14 16" fill="none" stroke="#fff" stroke-width="5"/></svg>
  <svg class="hero-arrow abs" style="left:1140px" width="26" height="44" viewBox="0 0 26 44"><path d="M6 6l14 16L6 38" fill="none" stroke="#fff" stroke-width="5"/></svg>
</section>

<h2 class="intro-title abs">What is Tilebeam</h2>
<p class="intro-text abs">Curabitur vel mi sit amet magna malesuada ultrices Ut nisi erat fermentum vel congue id euismod in elit Fusce ultricies orci ac feugiat suscipit leo massa sodales</p>

<article class="feature-card abs" style="left:162px">
  <svg width="60" height="62" viewBox="0 0 60 62" fill="none" stroke="#0b3d91" stroke-width="2.5"><path d="M4 58h54"/><rect x="8" y="44" width="8" height="14"/><rect x="22" y="36" width="8" height="22"/><rect x="36" y="28" width="8" height="30"/><rect x="48" y="18" width="8" height="40"/><path d="M6 34 22 22l8 6L50 6"/><path d="M42 6h8v8"/></svg>
  <h3>Project Milestones</h3>
  <p>Lorem ipsum dolor sit amet consectet uer adipiscing elit Nam</p>
  <a class="btn btn-blue" href="#">Learn More</a>
</article>
<article class="feature-card is-featured abs" style="left:477px">
  <svg width="56" height="56" viewBox="0 0 56 56" fill="none" stroke="#fff" stroke-width="2.5"><rect x="3" y="3" width="50" height="38"/><path d="M22 41v7h12v-7M16 52h24"/><rect x="11" y="11" width="6" height="6"/><path d="M22 14h18"/><rect x="11" y="24" width="6" height="6"/><path d="M22 27h22"/></svg>
  <h3>Track projects</h3>
  <p>Lorem ipsum dolor sit amet consectet uer adipiscing elit Nam</p>
  <a class="btn btn-light" href="#">Learn More</a>
</article>
<article class="feature-card abs" style="left:793px">
  <svg width="66" height="66" viewBox="0 0 66 66" fill="none" stroke="#0b3d91" stroke-width="2.5"><circle cx="33" cy="33" r="30"/><path d="M20 34l9 9 18-19"/></svg>
  <h3>Autoschedule tasks</h3>
  <p>Lorem ipsum dolor sit amet consectet uer adipiscing elit Nam</p>
  <a class="btn btn-blue" href="#">Learn More</a>
</article>

<div class="band-light abs"></div>
<div class="video-frame abs" role="img" aria-label="Product video still of a team meeting around a table"></div>
<svg class="play-button abs" width="86" height="86" viewBox="0 0 86 86"><circle cx="43" cy="43" r="40" fill="none" stroke="#fff" stroke-width="4"/><path d="M35 28v30l22-15z" fill="none" stroke="#fff" stroke-width="4" stroke-linejoin="round"/></svg>

<section class="why">
  <div class="why-photo abs" role="img" aria-label="Photo of two colleagues reviewing documents and a tablet"></div>
  <h2 class="why-title abs">Why We Are</h2>
  <p class="why-text abs" style="top:1808px">Curabitur vel mi sit amet magna malesuada ultrices Ut nisi erat fermentum vel congue id euismod in elit Fusce ultricies orci ac feugiat suscipit leo massa sodales velit et</p>
  <p class="why-text abs" style="top:1919px">Acelerisque quam Curabitur vel dolor ultrices ipsum dictum tristique Praesent vitae lacus Ut velit enim vestibulum non fermentum nec hendrerit quis leo Pellentesque rutru</p>
  <a class="btn btn-blue abs" href="#">Learn More</a>
</section>

<section class="testimonials">
  <h2 class="testi-title abs">What People Says</h2>
  <svg class="abs" style="left:182px;top:2404px" width="26" height="48" viewBox="0 0 26 48"><path d="M22 4 4 24l18 20" fill="none" stroke="#8a8f96" stroke-width="2.5"/></svg>
  <svg class="abs" style="left:960px;top:2404px" width="26" height="48" viewBox="0 0 26 48"><path d="M4 4l18 20L4 44" fill="none" stroke="#8a8f96" stroke-width="2.5"/></svg>
  <figure class="testi-card abs">
    <div class="avatar abs" role="img" aria-label="Portrait of the reviewer"></div>
    <span class="quote-mark abs" style="left:32px;top:72px">“</span>
    <span class="quote-mark abs" style="left:438px;top:135px">”</span>
    <blockquote class="testi-quote abs">One of my favorite features with this software is the locator. Having the costs customized to your location is so handy and much more accurate than applying a general multiplier to each item</blockquote>
    <div class="stars abs">
      <svg width="18" height="18" viewBox="0 0 24 24"><path fill="#f08a1c" d="M12 2l3 7h7l-5.6 4.4L18.5 21 12 16.8 5.5 21l2.1-7.6L2 9h7z"/></svg>
      <svg width="18" height="18" viewBox="0 0 24 24"><path fill="#f08a1c" d="M12 2l3 7h7l-5.6 4.4L18.5 21 12 16.8 5.5 21l2.1-7.6L2 9h7z"/></svg>
      <svg width="18" height="18" viewBox="0 0 24 24"><path fill="#f08a1c" d="M12 2l3 7h7l-5.6 4.4L18.5 21 12 16.8 5.5 21l2.1-7.6L2 9h7z"/></svg>
      <svg width="18" height="18" viewBox="0 0 24 24"><path fill="#f08a1c" d="M12 2l3 7h7l-5.6 4.4L18.5 21 12 16.8 5.5 21l2.1-7.6L2 9h7z"/></svg>
    </div>
    <figcaption>
      <div class="testi-name abs">Marisol K.</div>
      <div class="testi-role abs">Accounting Associate</div>
    </figcaption>
  </figure>
</section>

<section class="access abs" role="img" aria-label="Blue-toned photo of a woman using a tablet over a city skyline">
  <h2 class="access-title abs">Access from anywhere, anytime</h2>
  <p class="access-text abs" style="top:172px">Curabitur vel mi sit amet magna malesuada ultrices Ut nisi erat fermentum vel congue id euismod in elit Fusce</p>
  <p class="access-text abs" style="top:244px">ultricies orci ac feugiat suscipit leo massa sodales velit et scelerisque quam Curabitur vel dolor ultrices ipsum dictum tristique Praesent vitae lacus Ut velit enim vestibulum non fermentum nec</p>
  <a class="btn btn-light abs" href="#">Learn More</a>
</section>

<footer class="site-footer abs">
  <a class="brand abs" href="#"><span class="brand-square"></span>Tilebeam</a>
  <p class="footer-about abs">Praesent sit amet est In dictum dolor eu dictum porttitor enim felis viverra mi eget luctus massa purus quis odio Etiam nulla mas</p>
  <div class="footer-col abs" style="left:511px;top:56px">
    <h4>Company</h4>
    <ul><li>About Us</li><li>Our Products</li><li>Services</li><li>Partners</li><li>Contact</li></ul>
  </div>
  <div class="footer-col abs" style="left:677px;top:56px">
    <h4>Resources</h4>
    <ul><li>Support</li><li>Register</li><li>Free Trail</li><li>Sitemap</li></ul>
  </div>
  <div class="footer-col abs" style="left:859px;top:56px">
    <h4>Contact Us</h4>
    <ul><li>(555) 014 2280</li><li>hello@tilebeam.com</li></ul>
    <div class="social"><span></span><span></span><span></span><span></span></div>
  </div>
</footer>
<div class="footer-bar abs">© 2020 Company Name&nbsp; All right reserved</div>

</body>
</html>
```